New Zealand Export company needs business cards

We need new business cards to match our new logo for a company based in New Zealand who deal specifically with the Pacific Islands. We source, consolidate and ship products out of New Zealand to the Pacific Islands. Will attach our old ones and also new logo.
Would like the Islands we deal with and the areas of work we have access to, to be included on the business cards.

Contact Information for Business Card

T +64 9 381 5047
F +64 9 381 6620
12-18 Marlow Lane, Drury, 2113
PO Box 862, Drury, Auckland 2247, New Zealand
www.kestaltrade.co.nz
E sales@kestaltrade.co.nz

Font styles to use
Sans Serif

Colors
85abd2
33a6d7
ffffff

Requirements
Must have
• A company of WMB

```html
<!DOCTYPE html>
<html lang="en">
<head>
<meta charset="utf-8">
<title>Kestal Trade – Business Card</title>
<link rel="stylesheet" href="https://fonts.googleapis.com/css2?family=Arimo:wght@400;700&display=swap">
<style>
  :root {
    --backdrop: #fbf2d0;
    --card: #ffffff;
    --brand-blue: #1b5fa8;
    --sky: #33a6d7;
    --soft-blue: #85abd2;
    --bar-blue: #0f7cc0;
    --band-dark: #133f5f;
    --white: #ffffff;
  }
  * { box-sizing: border-box; margin: 0; padding: 0; }
  html, body { width: 900px; height: 1200px; overflow: hidden; }
  body {
    background: var(--backdrop);
    font-family: "Arimo", Arial, sans-serif;
    position: relative;
  }
  .card {
    position: absolute;
    left: 26px;
    width: 840px;
    height: 480px;
    background: var(--card);
    box-shadow: 6px 8px 10px rgba(0,0,0,0.35);
    overflow: hidden;
  }
  .card--front { top: 56px; }
  .card--back { top: 617px; }

  .side-bar {
    position: absolute;
    top: 147px;
    height: 237px;
    background: linear-gradient(180deg, var(--bar-blue), #1284c6);
  }
  .side-bar--left { left: 0; width: 95px; }
  .side-bar--right { right: 0; width: 92px; }

  .brand {
    position: absolute;
    left: 0; right: 0;
    display: flex;
    align-items: center;
    justify-content: center;
  }
  .brand__mark {
    background: var(--sky);
    margin-right: 18px;
  }
  .brand__name {
    color: var(--brand-blue);
    font-weight: 700;
    letter-spacing: 2px;
    white-space: nowrap;
  }
  .tagline {
    position: absolute;
    left: 0; right: 0;
    text-align: center;
    color: var(--soft-blue);
  }

  .card--front .brand { top: 168px; }
  .card--front .brand__mark { width: 44px; height: 44px; }
  .card--front .brand__name { font-size: 52px; }
  .card--front .tagline { top: 280px; font-size: 28px; }

  .card--back .brand { top: 72px; }
  .card--back .brand__mark { width: 34px; height: 34px; }
  .card--back .brand__name { font-size: 40px; }
  .card--back .tagline { top: 171px; font-size: 22px; }

  .contact-band {
    position: absolute;
    left: 0; bottom: 0;
    width: 840px; height: 209px;
  }
  .contact-band__bg { position: absolute; left: 0; top: 0; }
  .address {
    position: absolute;
    left: 75px; top: 55px;
    color: var(--white);
    font-size: 19px;
    line-height: 24px;
  }
  .contact-list {
    position: absolute;
    left: 468px; top: 16px;
    list-style: none;
    color: var(--white);
    font-size: 22px;
  }
  .contact-list li {
    display: flex;
    align-items: center;
    height: 37px;
    white-space: nowrap;
  }
  .contact-icon {
    flex: 0 0 20px;
    width: 20px; height: 20px;
    margin-right: 24px;
    fill: none;
    stroke: var(--white);
    stroke-width: 1.6;
    stroke-linejoin: round;
  }
</style>
</head>
<body>

<section class="card card--front">
  <div class="side-bar side-bar--left"></div>
  <div class="side-bar side-bar--right"></div>
  <div class="brand">
    <span class="brand__mark"></span>
    <span class="brand__name">KESTAL TRADE</span>
  </div>
  <p class="tagline">A Company of WMB</p>
</section>

<section class="card card--back">
  <div class="brand">
    <span class="brand__mark"></span>
    <span class="brand__name">KESTAL TRADE</span>
  </div>
  <p class="tagline">A Company of WMB</p>

  <div class="contact-band">
    <svg class="contact-band__bg" width="840" height="209" viewBox="0 0 840 209" aria-hidden="true">
      <defs>
        <linearGradient id="band-fill" x1="0" y1="0" x2="1" y2="0">
          <stop offset="0" stop-color="#0e6aa5"/>
          <stop offset="1" stop-color="#0a80c4"/>
        </linearGradient>
      </defs>
      <rect width="840" height="209" fill="url(#band-fill)"/>
      <polygon points="0,0 195,0 85,209 0,209" fill="#133f5f"/>
      <polygon points="195,0 335,0 240,209 85,209" fill="#175a85"/>
      <polygon points="335,0 470,0 320,209 240,209" fill="#0f6a9f"/>
    </svg>
    <p class="address">12-18 Marlow Lane, Drury, 2113<br>PO Box 862, Drury, Auckland 2247,<br>New Zealand</p>
    <ul class="contact-list">
      <li>
        <svg class="contact-icon" viewBox="0 0 20 20" aria-hidden="true"><path d="M5 2l3 3-2 2c1 3 3 5 6 6l2-2 3 3-2 3C8 17 3 12 2 5z"/></svg>
        <span>+64 9 381 5047</span>
      </li>
      <li>
        <svg class="contact-icon" viewBox="0 0 20 20" aria-hidden="true"><rect x="2" y="7" width="16" height="11"/><rect x="6" y="2" width="8" height="5"/><path d="M6 11h8M6 14h8"/></svg>
        <span>+64 9 381 6620</span>
      </li>
      <li>
        <svg class="contact-icon" viewBox="0 0 20 20" aria-hidden="true"><rect x="2" y="6" width="16" height="12"/><path d="M2 6l8 7 8-7"/></svg>
        <span>sales@kestaltrade.co.nz</span>
      </li>
      <li>
        <svg class="contact-icon" viewBox="0 0 20 20" aria-hidden="true"><circle cx="10" cy="10" r="8"/><ellipse cx="10" cy="10" rx="3.5" ry="8"/><path d="M2 10h16"/></svg>
        <span>www.kestaltrade.co.nz</span>
      </li>
    </ul>
  </div>
</section>

</body>
</html>
```